Retail and Ecommerce Archery Shop needs new Home Page Design

We need a homepage design created for an existing company named Harlow Ridge Sport Depot. They sell various types of Archery equipment for both Bow hunting and Target shooting both in store and online. They offer shooting lessons, have an indoor archery shooting range with memberships available, and have their own line of bowstrings. For color scheme, use the current home page as inspiration. The Homepage Template has links to specific images, if any other images are needed, stock images are acceptable.

Current Website: https://hrsportdepot.com/

Customer Avatar: https://files.norvexa.com/doc/d/7Tq2Wm9XbR4LpZ8vKc3NhY6JfG1sDe5AaUoPiQwErTy/view?mode=share

Core Message Canvas: https://files.norvexa.com/sheet/d/4K_718bnRz962T3w57nLqX8hjd4Mc2Vb7wP0gE3R_uHz/view?mode=share

Homepage Template-Use this worksheet as the structue of the homepage: https://files.norvexa.com/doc/d/9pLxTrWq2N8mHc4ZbVs5KdYo7GfEjU3RaCiAwB6nMeQ/view?mode=share

```html
<!DOCTYPE html>
<html lang="en">
<head>
<meta charset="utf-8">
<title>Harlow Ridge Sport Depot — Home</title>
<link rel="stylesheet" href="https://fonts.googleapis.com/css2?family=Merriweather:wght@400;700;900&family=Lato:wght@400;700&display=swap">
<style>
:root{
  --yellow:#f5c70d;
  --blue:#0a86c8;
  --blue-dark:#0670ad;
  --ink:#111111;
  --text:#333333;
  --white:#ffffff;
  --grey-bg:#f2f2f2;
  --footer:#101010;
  --serif:'Merriweather', Georgia, serif;
  --sans:'Lato', Arial, sans-serif;
}
*{box-sizing:border-box;margin:0;padding:0}
html,body{width:1200px;height:3854px;overflow:hidden;background:var(--white)}
body{position:relative;font-family:var(--serif);color:var(--ink)}
a{color:inherit;text-decoration:none}
.abs{position:absolute}

/* Hero */
.hero{position:absolute;left:0;top:0;width:1200px;height:606px;overflow:hidden}
.hero-photo{position:absolute;inset:0;background:
  radial-gradient(ellipse at 70% 40%, #6b5a45 0%, #3c3a2c 35%, #22251d 70%),
  #2a2b22}
.hero-flowers{position:absolute;left:380px;bottom:0;width:820px;height:200px;
  background:linear-gradient(180deg,rgba(120,110,160,0) 0%,rgba(110,100,150,.55) 60%,rgba(70,80,60,.8) 100%)}
.hero-wedge{position:absolute;inset:0}
.brand{position:absolute;left:112px;top:26px;font-family:var(--serif);font-weight:700;color:var(--yellow);font-size:19px;line-height:1.15;width:200px}
.brand-dot{display:inline-block;width:12px;height:12px;border-radius:50%;background:var(--yellow);margin-right:8px;vertical-align:middle}
.nav{position:absolute;top:33px;left:440px;display:flex;font-size:15px;color:var(--white);letter-spacing:.2px}
.nav a{margin-right:51px}
.nav a:last-child{margin-right:0}
.hero-title{position:absolute;left:112px;top:306px;font-weight:900;font-size:34px;line-height:42px;color:var(--white);text-shadow:0 2px 3px rgba(0,0,0,.35)}
.hero-sub{position:absolute;left:112px;top:404px;font-size:12.5px;color:var(--white);font-weight:700}
.hero-btns{position:absolute;left:112px;top:438px;display:flex;gap:20px}
.btn-white{background:var(--white);color:var(--ink);border-radius:24px;font-weight:700;font-size:14px;height:44px;padding:0 20px;display:flex;align-items:center}
.btn-outline{border:2px solid var(--white);color:var(--ink);border-radius:24px;font-weight:700;font-size:14px;height:44px;padding:0 18px;display:flex;align-items:center}

/* Section headings */
.divider{position:absolute;left:552px;width:96px;height:6px;border-radius:3px;background:var(--yellow)}
.sec-title{position:absolute;left:0;width:1200px;text-align:center;font-size:38px;font-weight:400;color:var(--ink)}
.sec-title b{font-weight:900}

/* Partners */
.partners{position:absolute;left:112px;top:772px;width:976px;display:flex;justify-content:space-between;align-items:center}
.partner{height:52px;background:#d9d9d9;border-radius:8px}

/* Services */
.hex{position:absolute;width:212px;height:236px}
.hex-shape{position:absolute;left:0;top:0;width:212px;height:236px}
.hex-icon{position:absolute;left:71px;top:54px;width:70px;height:70px}
.hex-label{position:absolute;left:24px;right:24px;text-align:center;font-weight:700;font-size:15px;line-height:25px}

.btn-yellow{position:absolute;background:var(--yellow);color:var(--ink);font-weight:700;font-size:20px;border-radius:34px;display:flex;align-items:center;justify-content:center;box-shadow:0 4px 8px rgba(0,0,0,.18)}

/* Bowstrings */
.band{position:absolute;left:0;top:1643px;width:1200px;height:372px;background:linear-gradient(120deg,var(--blue-dark) 0%,var(--blue) 50%,var(--blue-dark) 100%)}
.video{position:absolute;left:112px;top:1807px;width:976px;height:407px;border:3px solid var(--yellow);overflow:hidden;background:linear-gradient(180deg,#4a4a48 0%,#6b4a3c 35%,#3d3b38 60%,#2a2a28 100%)}
.video-brand{position:absolute;right:22px;top:38px;font-weight:700;font-size:18px;color:var(--yellow)}
.play{position:absolute;left:571px;top:1982px;width:58px;height:58px;border-radius:50%;background:var(--yellow);box-shadow:0 0 0 8px rgba(245,199,13,.35)}

/* Welcome cards */
.subtitle{position:absolute;left:0;width:1200px;text-align:center;font-weight:700;font-size:16px}
.card{position:absolute;top:2450px;width:292px;background:var(--white);border-radius:8px;box-shadow:0 4px 14px rgba(0,0,0,.14);padding:24px 20px;text-align:center}
.card h3{font-size:18px;font-weight:400;line-height:31px;color:var(--ink);margin-bottom:2px}
.card p{font-family:var(--sans);font-size:14px;line-height:30px;color:var(--text)}
.card-bar{position:absolute;height:14px;border-radius:0 0 8px 8px}

/* Newsletter */
.news{position:absolute;left:0;top:3052px;width:1200px;height:404px;background:var(--grey-bg)}
.news-title{position:absolute;left:0;top:3138px;width:1200px;text-align:center;font-size:35px;line-height:47px;font-weight:400}
.news-title b{font-weight:900}
.news-sub{position:absolute;left:0;top:3253px;width:1200px;text-align:center;font-size:15px}
.news-form{position:absolute;left:192px;top:3306px;width:813px;height:63px;background:var(--white);border-radius:32px;box-shadow:0 3px 10px rgba(0,0,0,.12)}
.news-form span{position:absolute;left:22px;top:22px;font-size:14px;font-weight:700}
.news-form .go{position:absolute;right:6px;top:6px;width:150px;height:51px;background:var(--yellow);border-radius:26px;font-weight:900;font-size:18px;display:flex;align-items:center;justify-content:center}

/* Footer */
.footer{position:absolute;left:0;top:3456px;width:1200px;height:398px;background:var(--footer);color:var(--white)}
.f-col{position:absolute;top:70px}
.f-col h4{font-weight:400;font-size:20px;margin-bottom:18px}
.f-col li{list-style:none;font-size:14.5px;line-height:34px;padding-left:4px}
.f-col li::before{content:"»";margin-right:10px;font-weight:700}
.contact{position:absolute;left:693px;top:112px;font-size:14.5px}
.c-row{display:flex;align-items:flex-start;gap:14px;margin-bottom:22px;line-height:23px}
.c-ico{width:30px;height:30px;border-radius:50%;background:var(--white);flex:none;display:flex;align-items:center;justify-content:center}
.f-brand{position:absolute;left:923px;top:100px;width:160px;font-weight:700;font-size:17px;line-height:21px;color:var(--yellow)}
.socials{position:absolute;left:925px;top:156px;display:flex;gap:21px}
.socials span{width:25px;height:25px;border-radius:50%;background:var(--white)}
.f-rule{position:absolute;left:110px;top:323px;width:978px;height:1px;background:#555}
.copy{position:absolute;left:0;top:352px;width:1200px;text-align:center;font-size:14px}
</style>
</head>
<body>

<svg width="0" height="0" style="position:absolute" aria-hidden="true">
  <defs><filter id="sh" x="-20%" y="-20%" width="140%" height="140%"><feDropShadow dx="0" dy="4" stdDeviation="6" flood-opacity=".18"/></filter></defs>
</svg>

<header class="hero">
  <div class="hero-photo" role="img" aria-label="Bow hunter in camouflage drawing a compound bow in a forest with purple wildflowers"></div>
  <div class="hero-flowers"></div>
  <svg class="hero-wedge" width="1200" height="606" viewBox="0 0 1200 606" aria-hidden="true">
    <polygon points="0,306 561,187 479,606 0,606" fill="#f5c70d"/>
  </svg>
  <div class="brand"><span class="brand-dot"></span>Harlow Ridge Sport Depot</div>
  <nav class="nav">
    <a href="#">SHOP</a><a href="#">ABOUT US</a><a href="#">RANGE</a><a href="#">PRO SHOP</a><a href="#">ELECTRIC BOWSTRINGS</a>
  </nav>
  <h1 class="hero-title">Your Bow Hunting<br>Adventure Starts Here</h1>
  <p class="hero-sub">Top-Notch Equipment • Expertise • Unmatched Support</p>
  <div class="hero-btns">
    <a class="btn-white" href="#">Indoor Archery Range</a>
    <a class="btn-outline" href="#">Shop Our Bows</a>
  </div>
</header>

<section class="pro-shop">
  <div class="divider" style="top:684px"></div>
  <h2 class="sec-title" style="top:702px">We Are a <b>Full-Service Archery</b> Pro Shop</h2>
  <div class="partners" aria-label="Partner brands">
    <div class="partner" style="width:108px"></div>
    <div class="partner" style="width:148px;border-radius:26px"></div>
    <div class="partner" style="width:134px"></div>
    <div class="partner" style="width:138px"></div>
    <div class="partner" style="width:78px"></div>
    <div class="partner" style="width:102px"></div>
  </div>
</section>

<section class="services">
  <div class="divider" style="top:904px"></div>
  <h2 class="sec-title" style="top:922px">Our <b>Service</b></h2>

  <div class="hex" style="left:111px;top:985px">
    <svg class="hex-shape" viewBox="0 0 212 236" aria-hidden="true">
      <polygon points="106,4 208,62 208,174 106,232 4,174 4,62" fill="#fff" filter="url(#sh)"/>
      <polygon points="106,20 194,70 194,166 106,216 18,166 18,70" fill="#f5c70d"/></svg>
    <svg class="hex-icon" viewBox="0 0 70 70" fill="none" stroke="#111" stroke-width="3" stroke-linecap="round" aria-hidden="true"><path d="M10 12 Q48 10 58 58"/><path d="M10 12 L58 58"/><path d="M14 56 L54 16"/><path d="M54 16 l-9 1 M54 16 l-1 9"/></svg>
    <div class="hex-label" style="top:140px">Bow setup and sizing</div>
  </div>
  <div class="hex" style="left:365px;top:985px">
    <svg class="hex-shape" viewBox="0 0 212 236" aria-hidden="true"><polygon points="106,4 208,62 208,174 106,232 4,174 4,62" fill="#fff" filter="url(#sh)"/>
      <polygon points="106,20 194,70 194,166 106,216 18,166 18,70" fill="#0a86c8"/></svg>
    <svg class="hex-icon" viewBox="0 0 70 70" fill="none" stroke="#fff" stroke-width="3" aria-hidden="true"><circle cx="33" cy="33" r="22" stroke-dasharray="8 4"/><circle cx="33" cy="33" r="12"/><circle cx="50" cy="50" r="10" fill="#0a86c8"/><path d="M45 50 l4 4 l7 -8"/></svg>
    <div class="hex-label" style="top:128px;color:#fff">D-loop and peep sight installs</div>
  </div>
  <div class="hex" style="left:623px;top:985px">
    <svg class="hex-shape" viewBox="0 0 212 236" aria-hidden="true"><polygon points="106,4 208,62 208,174 106,232 4,174 4,62" fill="#fff" filter="url(#sh)"/>
      <polygon points="106,20 194,70 194,166 106,216 18,166 18,70" fill="#f5c70d"/></svg>
    <svg class="hex-icon" viewBox="0 0 70 70" fill="none" stroke="#111" stroke-width="3" aria-hidden="true"><rect x="8" y="8" width="54" height="54" rx="3"/><path d="M8 20 H62"/><circle cx="28" cy="42" r="9"/><path d="M46 28 V56 M54 28 V56"/></svg>
    <div class="hex-label" style="top:140px">Accessory installs</div>
  </div>
  <div class="hex" style="left:880px;top:985px">
    <svg class="hex-shape" viewBox="0 0 212 236" aria-hidden="true"><polygon points="106,4 208,62 208,174 106,232 4,174 4,62" fill="#fff" filter="url(#sh)"/>
      <polygon points="106,20 194,70 194,166 106,216 18,166 18,70" fill="#0a86c8"/></svg>
    <svg class="hex-icon" viewBox="0 0 70 70" fill="none" stroke="#fff" stroke-width="4" stroke-linecap="round" stroke-linejoin="round" aria-hidden="true"><path d="M18 36 V20 H56 M48 12 l8 8 l-8 8"/><path d="M52 34 V50 H14 M22 42 l-8 8 l8 8"/></svg>
    <div class="hex-label" style="top:140px;color:#fff">Cam/limb swaps</div>
  </div>

  <div class="hex" style="left:240px;top:1207px">
    <svg class="hex-shape" viewBox="0 0 212 236" aria-hidden="true"><polygon points="106,4 208,62 208,174 106,232 4,174 4,62" fill="#fff" filter="url(#sh)"/>
      <polygon points="106,20 194,70 194,166 106,216 18,166 18,70" fill="#0a86c8"/></svg>
    <svg class="hex-icon" viewBox="0 0 70 70" fill="none" stroke="#fff" stroke-width="4" stroke-linecap="round" aria-hidden="true"><path d="M54 28 A21 21 0 0 0 18 20"/><path d="M16 42 A21 21 0 0 0 52 50"/><path d="M18 10 V20 H28 M52 60 V50 H42"/></svg>
    <div class="hex-label" style="top:146px;color:#fff">String swaps</div>
  </div>
  <div class="hex" style="left:494px;top:1207px">
    <svg class="hex-shape" viewBox="0 0 212 236" aria-hidden="true"><polygon points="106,4 208,62 208,174 106,232 4,174 4,62" fill="#fff" filter="url(#sh)"/>
      <polygon points="106,20 194,70 194,166 106,216 18,166 18,70" fill="#f5c70d"/></svg>
    <svg class="hex-icon" viewBox="0 0 70 70" fill="none" stroke="#111" stroke-width="4" stroke-linecap="round" aria-hidden="true"><path d="M6 18 H64 M6 35 H64 M6 52 H64"/><path d="M22 10 V26 M46 27 V43 M54 44 V60"/></svg>
    <div class="hex-label" style="top:140px">Paper tuning</div>
  </div>
  <div class="hex" style="left:751px;top:1207px">
    <svg class="hex-shape" viewBox="0 0 212 236" aria-hidden="true"><polygon points="106,4 208,62 208,174 106,232 4,174 4,62" fill="#fff" filter="url(#sh)"/>
      <polygon points="106,20 194,70 194,166 106,216 18,166 18,70" fill="#0a86c8"/></svg>
    <svg class="hex-icon" viewBox="0 0 70 70" fill="none" stroke="#fff" stroke-width="3.5" stroke-linecap="round" stroke-linejoin="round" aria-hidden="true"><rect x="5" y="5" width="60" height="60" rx="8"/><path d="M16 35 H54"/><path d="M35 12 V30 M28 19 l7 -7 l7 7"/><path d="M35 40 V58 M28 51 l7 7 l7 -7"/></svg>
    <div class="hex-label" style="top:134px;color:#fff">2nd/3rd axis Adjustments</div>
  </div>

  <a class="btn-yellow" href="#" style="left:503px;top:1504px;width:194px;height:63px">View More</a>
</section>

<section class="bowstrings">
  <div class="band"></div>
  <div class="divider" style="top:1708px;background:#fff"></div>
  <h2 class="sec-title" style="top:1733px;color:#fff">Our Custom <b>Electric Bowstrings</b></h2>
  <div class="video" role="img" aria-label="Video still of a bowstring being built on a jig with green posts and orange strands">
    <div class="video-brand">Harlow Ridge Sport Depot</div>
  </div>
  <div class="play"></div>
  <svg class="abs" style="left:593px;top:2000px" width="18" height="22" viewBox="0 0 18 22" aria-hidden="true"><polygon points="2,1 17,11 2,21" fill="#fff"/></svg>
  <a class="btn-yellow" href="#" style="left:420px;top:2183px;width:360px;height:63px">Shop Our Custom Bowstrings</a>
</section>

<section class="welcome">
  <div class="divider" style="top:2313px"></div>
  <h2 class="sec-title" style="top:2334px">Welcome to your <b>local Archery Shop</b></h2>
  <p class="subtitle" style="top:2400px">Where consistency is built</p>

  <div class="card-bar" style="left:146px;top:2750px;width:240px;background:var(--blue)"></div>
  <article class="card" style="left:112px;height:302px">
    <h3>Looking for a new Bow setup?</h3>
    <p>Our custom bow-fitting process will be perfect for you. We get you set up the right way, the first time! We will get your measurements, check your shot, and make sure you leave feeling confident with your new Bow!</p>
  </article>

  <div class="card-bar" style="left:488px;top:2766px;width:240px;background:var(--yellow)"></div>
  <article class="card" style="left:453px;height:318px">
    <h3>Looking to make some improvements to your current archery setup?</h3>
    <p>We have access to almost all of the popular archery accessories on the market! We don't sell anything we wouldn't use ourselves so come on in and talk with our shop experts to figure out what will work best for you.</p>
  </article>

  <div class="card-bar" style="left:830px;top:2841px;width:240px;background:var(--blue)"></div>
  <article class="card" style="left:794px;height:393px">
    <h3>Are you looking to improve your shot? Reserve some time on our range!</h3>
    <p>Before you step into the field to take your first shot of the season, take time to go to the range. Archery, like any skill, requires practice &amp; diligence to develop a consistent &amp; confident shot. We have a 12-lane 20-yard indoor range in the shop. Daily Range and memberships are available. We also offer bow rental and lessons.</p>
  </article>

  <a class="btn-yellow" href="#" style="left:476px;top:2913px;width:245px;height:63px">Range Information</a>
</section>

<section class="news"></section>
<div class="divider" style="top:3114px"></div>
<h2 class="news-title">Join Our Archery Community: <b>Exclusive Deals, Tips,<br>and Updates Straight to Your Inbox!</b></h2>
<p class="news-sub">Join today &amp; stay up-to-date on new product releases, shop promotions, and our archery newsletters</p>
<form class="news-form">
  <span>Enter The Email</span>
  <div class="go">Subscribe</div>
</form>

<footer class="footer">
  <div class="f-col" style="left:109px">
    <h4>Quick Links</h4>
    <ul><li>Home</li><li>About</li><li>Range</li><li>Pro Shop</li><li>Contact us</li></ul>
  </div>
  <div class="f-col" style="left:265px">
    <h4>Services</h4>
    <ul><li>Paper tuning</li><li>Cam/limb swaps</li><li>String swaps</li><li>Building, tuning</li><li>Accessory installs</li></ul>
  </div>
  <div class="f-col" style="left:465px">
    <h4>Help Links</h4>
    <ul><li>FAQ</li><li>Terms of use</li><li>Privacy Policy</li><li>Support Links</li><li>Miscellaneous Information</li></ul>
  </div>
  <div class="f-col" style="left:693px"><h4>Contact Us</h4></div>
  <div class="contact">
    <div class="c-row"><span class="c-ico"><svg width="14" height="18" viewBox="0 0 14 18"><path d="M7 1 a6 6 0 0 1 6 6 c0 4 -6 10 -6 10 s-6 -6 -6 -10 a6 6 0 0 1 6 -6z" fill="#111"/><circle cx="7" cy="7" r="2.2" fill="#fff"/></svg></span><span>4127 W. Route 9<br>Millbrook, KS 66999</span></div>
    <div class="c-row" style="align-items:center"><span class="c-ico"><svg width="16" height="16" viewBox="0 0 16 16"><path d="M3 1 l3 0 l1 4 l-2 1.5 a9 9 0 0 0 4.5 4.5 l1.5 -2 l4 1 l0 3 a2 2 0 0 1 -2 2 a13 13 0 0 1 -12 -12 a2 2 0 0 1 2 -2z" fill="#111"/></svg></span><span>(555)-014-0288</span></div>
    <div class="c-row" style="align-items:center"><span class="c-ico"><svg width="16" height="12" viewBox="0 0 16 12"><rect x="0" y="0" width="16" height="12" rx="1.5" fill="#111"/><path d="M1 1 l7 6 l7 -6" stroke="#fff" stroke-width="1.4" fill="none"/></svg></span><span>hello@hrsportdepot.com</span></div>
  </div>
  <div class="f-brand">Harlow Ridge Sport Depot</div>
  <div class="socials" aria-label="Social links"><span></span><span></span><span></span><span></span></div>
  <div class="f-rule"></div>
  <p class="copy">Copyrights@2023.Harlow Ridge Sport Depot.All Rights Reserved</p>
</footer>

</body>
</html>
```